New Custom Pizza Box Design Project For Independant Restaurant

We are looking for creative designs for our new custom printed pizza boxes. Designs should include the following:

-Our logo & company name
-A color scheme similar to our current logo
-Our physical and URL addresses & phone number (menu is attached)
-Ability to scale the design across several box sizes (10x10x2, 14x14x2, 18x13x2,
26x18x2)
- Any creative flair you think will make for the best design

Design can be on a white or kraft (tan) box.
Designs can be either two or three ink colors.

***Please note, designs must be able to be screen printed on boxes***
Updates

Reason: Still debating which to choose

Target Market(s)

Designs do not have to be targeted to any specific demographic.

Industry/Entity Type

Pizza Delivery

Font styles to use
Other font styles liked:
• Please use font similar to our logo text

Requirements
Must have
• -2 or 3 ink colors
• -company name, address, phone number, URL
• -company logo and colors
• -flexibility to use on different box sizes (10x10x2, 14x14x2, 18x13x2,
• 26x18x2)
• -utilize full printable area on boxes (including 2" dimension on box sides)
• ***Please note, designs must be able to be screen printed on boxes***
Should not have
• Design features with strong similarities to existing designs of other pizzerias

```html
<!DOCTYPE html>
<html lang="en">
<head>
<meta charset="utf-8">
<title>Marco's Henhouse Pizzeria – Pizza Box</title>
<link href="https://fonts.googleapis.com/css2?family=Saira+Condensed:wght@700;800&family=Saira+Semi+Condensed:wght@700&display=swap" rel="stylesheet">
<style>
  :root {
    --backdrop-top: #5a4b3d;
    --backdrop-bottom: #2e2016;
    --kraft: #cbb99f;
    --kraft-light: #d8c9b2;
    --kraft-ghost: #b8a586;
    --ink: #3a2a1d;
  }
  html, body {
    margin: 0;
    width: 1200px;
    height: 946px;
    overflow: hidden;
  }
  body {
    background: radial-gradient(ellipse at 50% 0%, var(--backdrop-top), var(--backdrop-bottom) 70%);
    position: relative;
    font-family: "Saira Semi Condensed", "Saira Condensed", sans-serif;
    color: var(--ink);
  }
  .box-lid {
    position: absolute;
    left: 300px;
    top: 36px;
    width: 600px;
    height: 600px;
    background: linear-gradient(160deg, var(--kraft-light), var(--kraft));
    overflow: hidden;
  }
  .lid-ghost {
    position: absolute;
    inset: 0;
    display: flex;
    flex-direction: column;
    justify-content: center;
    align-items: center;
    font-family: "Saira Condensed", sans-serif;
    font-weight: 800;
    font-size: 150px;
    line-height: 0.95;
    color: var(--kraft-ghost);
    opacity: 0.55;
    text-align: center;
    letter-spacing: 4px;
  }
  .lid-brand {
    position: absolute;
    left: 0;
    right: 0;
    top: 50%;
    transform: translateY(-50%);
    display: flex;
    flex-direction: column;
    align-items: center;
    gap: 18px;
  }
  .brand-mark {
    width: 74px;
    height: 74px;
    border-radius: 50%;
    background: var(--ink);
  }
  .brand-name {
    font-family: "Saira Condensed", sans-serif;
    font-weight: 800;
    font-size: 58px;
    line-height: 0.95;
    text-align: center;
    letter-spacing: 3px;
    text-transform: uppercase;
    color: var(--ink);
  }
  .box-side {
    position: absolute;
    top: 690px;
    width: 560px;
    height: 130px;
    background: linear-gradient(180deg, var(--kraft-light), var(--kraft));
    display: flex;
    align-items: center;
    gap: 22px;
    padding: 0 26px;
    box-sizing: border-box;
  }
  .box-side--address { left: 30px; }
  .box-side--web { left: 610px; }
  .side-brand {
    display: flex;
    align-items: center;
    gap: 8px;
    flex-shrink: 0;
  }
  .side-brand .brand-mark {
    width: 22px;
    height: 22px;
  }
  .side-brand .brand-name {
    font-size: 20px;
    letter-spacing: 1px;
  }
  .side-text {
    font-weight: 700;
    font-size: 25px;
    white-space: nowrap;
  }
  .side-text--web {
    font-size: 38px;
  }
</style>
</head>
<body>
  <section class="box-lid" aria-label="Pizza box lid">
    <div class="lid-ghost" aria-hidden="true">
      <span>MARCO'S</span><span>HENHOUSE</span><span>PIZZERIA</span>
    </div>
    <div class="lid-brand">
      <div class="brand-mark"></div>
      <div class="brand-name">Marco's<br>Henhouse<br>Pizzeria</div>
    </div>
  </section>

  <section class="box-side box-side--address" aria-label="Box side with address">
    <div class="side-brand">
      <div class="brand-mark"></div>
      <div class="brand-name">Marco's<br>Henhouse</div>
    </div>
    <div class="side-text">1427 Alder Street Riverside Commons</div>
  </section>

  <section class="box-side box-side--web" aria-label="Box side with website">
    <div class="side-brand">
      <div class="brand-mark"></div>
      <div class="brand-name">Marco's<br>Henhouse</div>
    </div>
    <div class="side-text side-text--web">www.marcoshenhouse.com</div>
  </section>
</body>
</html>
```